Start a weight loss Clinic

build a landing page website using the content from this websites. we want to copy all the content from slimcarecourses.net but make page look more professional. we dont have a logo yet but url is www.launchyourtrimcenter.com
https://physiciansleanbodyalliance.com/home-page
https://www.slimcarecourses.net/

Target Market(s)

people looking to open a weightloss clinic or a franchise opportunity

Coding

Coded - Design and coding required

Number of Pages Required

3 page

Requirements
Must have
• copy all content from other site https://www.slimcarecourses.net/

```html
<!DOCTYPE html>
<html lang="en">
<head>
<meta charset="utf-8">
<title>Start Your Own Weight Loss Clinic</title>
<link href="https://fonts.googleapis.com/css2?family=Open+Sans:wght@400;600;700&family=Roboto+Slab:wght@400;500;600&display=swap" rel="stylesheet">
<style>
:root{
  --navy:#1b3a6b;
  --heading:#2c4f86;
  --blue:#2b86de;
  --btn-blue:#2f80d8;
  --red:#c8282b;
  --red-band:#d12e2e;
  --ink:#111;
  --grey-bg:#f4f4f4;
  --field:#efefef;
  --white:#fff;
}
*{box-sizing:border-box;margin:0;padding:0}
html,body{width:1200px;height:3608px;overflow:hidden;background:var(--white)}
body{position:relative;font-family:"Open Sans",sans-serif;color:var(--ink)}
.abs{position:absolute}
.slab{font-family:"Roboto Slab",serif}
.btn{position:absolute;display:flex;align-items:center;justify-content:center;font-family:"Roboto Slab",serif;font-weight:500;color:var(--white);border-radius:4px;text-decoration:none}

/* header */
.site-header{top:0;left:0;width:1200px;height:94px;background:var(--white)}
.brand{left:164px;top:32px}
.brand-name{font-family:"Roboto Slab",serif;font-weight:600;font-size:24px;color:var(--heading);line-height:30px;white-space:nowrap}
.call{display:flex;align-items:center;gap:10px}
.call small{display:block;font-size:11px;color:var(--btn-blue);font-weight:600}
.call strong{display:block;font-size:23px;color:var(--heading);font-weight:600;line-height:1.1}

/* hero */
.hero{top:94px;left:0;width:1200px;height:910px;background:linear-gradient(90deg,#eeeeec 0%,#e9e8e4 45%,#e4ddd2 70%,#d9cfc1 100%)}
.hero-photo{top:94px;left:700px;width:500px;height:910px;background:radial-gradient(ellipse at 55% 50%,#c9b9a8 0%,#ddd3c6 45%,rgba(233,232,228,0) 75%)}
.hero-kicker{left:156px;top:174px;font-size:31px;font-weight:500;color:var(--ink)}
.hero-title{left:156px;top:215px;font-size:44px;font-weight:600;color:var(--heading)}
.hero-copy{left:156px;top:294px;width:566px;font-size:15.5px;line-height:21px}
.hero-copy p{margin-bottom:7px}
.panel{left:156px;top:547px;width:562px;height:394px;background:var(--navy);border-radius:3px;padding:50px 32px 0 32px;color:var(--white)}
.panel-kicker{font-family:"Roboto Slab",serif;font-size:15px;color:#6fb3ff}
.panel-title{font-family:"Roboto Slab",serif;font-size:27px;font-weight:500;margin-top:10px}
.panel-copy{font-size:15px;line-height:21px;margin-top:22px}

/* offer */
.offer{top:1004px;left:0;width:1200px;height:645px;background:var(--grey-bg)}
.card{position:absolute;width:218px;height:218px;background:var(--white);box-shadow:0 2px 8px rgba(0,0,0,.08);padding:22px}
.card-label{position:absolute;left:23px;bottom:26px;font-family:"Roboto Slab",serif;font-weight:500;font-size:15px;line-height:20px}
.card svg{position:absolute;right:24px;top:26px}
.rule{height:3px;width:62px;background:var(--btn-blue)}
.offer-title{left:682px;top:1168px;font-size:35px;font-weight:500}
.offer-copy{left:682px;top:1223px;width:380px;font-size:11.5px;line-height:15.5px}
.ticks{left:682px;top:1304px;list-style:none;font-size:11.5px}
.ticks li{display:flex;align-items:center;gap:12px;height:23px}

/* steps */
.steps{left:155px;top:1687px;width:888px;height:328px;background:linear-gradient(135deg,#e3edf9 0%,#dbe6f6 100%);border-radius:3px}
.steps-title{left:0;top:34px;width:888px;text-align:center;font-size:34px;color:var(--heading)}
.step{position:absolute;top:102px;width:200px;text-align:center}
.step-num{width:42px;height:42px;margin:0 auto;border-radius:50%;border:2px solid var(--red);display:flex;align-items:center;justify-content:center}
.step-num span{width:34px;height:34px;border-radius:50%;background:var(--red);color:var(--white);font-family:"Roboto Slab",serif;font-size:22px;display:flex;align-items:center;justify-content:center}
.step h3{font-family:"Roboto Slab",serif;font-weight:500;font-size:15.5px;color:var(--heading);margin-top:16px}
.step p{font-size:10px;line-height:14px;color:#4a6fa5;margin-top:6px}

/* compare */
.compare{left:155px;top:2052px;width:888px;height:358px;background:linear-gradient(135deg,#d9e5f6 0%,#e6eef9 100%);border-radius:3px}
.compare-title{left:0;top:28px;width:888px;text-align:center;font-size:35px;color:var(--heading)}
.pill{position:absolute;width:218px;height:29px;border-radius:15px;background:var(--btn-blue);color:var(--white);font-size:12.5px;display:flex;align-items:center;justify-content:center;gap:12px}

/* contact */
.contact-title{left:156px;top:2500px;font-size:36px;font-weight:500}
.contact-sub{left:156px;top:2552px;font-size:10px}
.contact-item{display:flex;align-items:center;gap:10px;font-size:10px;line-height:14px}
.contact-item b{font-weight:600}
.contact-photo{left:155px;top:2691px;width:583px;height:155px;border-radius:4px;background:linear-gradient(90deg,#8a6a58 0%,#b58e78 35%,#c9a896 60%,#9c7766 100%)}
.form-card{left:762px;top:2472px;width:281px;height:374px;background:var(--white);box-shadow:0 2px 10px rgba(0,0,0,.1)}
.form-head{height:62px;background:var(--btn-blue);color:var(--white);display:flex;align-items:center;justify-content:center;font-family:"Roboto Slab",serif;font-weight:500;font-size:15px}
.field{position:absolute;left:32px;width:217px;height:29px;background:var(--field);font-size:10px;padding:8px 12px;color:#333}

/* partnership */
.partner-area{color:var(--white)}
.partner{top:2909px;left:0;width:1200px;height:507px;background:var(--blue)}
.partner-photo{left:600px;top:3020px;width:576px;height:396px;background:radial-gradient(ellipse at 50% 65%,#e9d5c6 0%,#cfb5a5 35%,rgba(43,134,222,0) 72%)}
.partner-kicker{left:158px;top:2986px;font-size:15px;font-weight:500}
.partner-title{left:158px;top:3010px;font-size:36px;font-weight:500;padding:0 4px;background:linear-gradient(180deg,transparent 82%,#1f5fa8 82%)}
.partner-copy{left:158px;top:3072px;width:352px;font-size:9.8px;line-height:13.5px}
.partner-copy p{margin-bottom:12px}
.offer-icon{left:158px;top:3253px;width:78px;height:78px;border-radius:50%;background:var(--white)}
.offer-detail{left:269px;top:3230px;width:240px;font-size:10px;line-height:13.5px}

/* invest */
.invest{top:3416px;left:0;width:1200px;height:192px;background:var(--red-band);color:var(--white);text-align:center}
.invest-title{position:absolute;top:32px;width:1200px;font-size:23px;font-weight:500}
.invest-foot{position:absolute;top:130px;width:1200px;font-size:22.5px;font-weight:500}
</style>
</head>
<body>

<header class="abs site-header">
  <div class="abs brand">
    <div class="brand-name">TrimPath Clinics</div>
  </div>
  <div class="abs call" style="left:693px;top:28px">
    <svg width="34" height="34" viewBox="0 0 34 34"><circle cx="17" cy="17" r="15.5" fill="none" stroke="#2f80d8" stroke-width="2"/><path d="M12 10c1-1 2-1 3 0l2 3c.5 1 0 2-1 2.5-.5.5 0 2 1.5 3.5s3 2 3.5 1.5c.5-1 1.5-1.5 2.5-1l3 2c1 1 1 2 0 3-3 3-8 1-12-3s-6-9-2.5-11.5z" fill="#2c4f86"/></svg>
    <div><small>Free Consultation</small><strong>877-555-0142</strong></div>
  </div>
  <a class="btn" style="left:909px;top:27px;width:134px;height:43px;background:var(--btn-blue);font-size:14px">Contact Us</a>
</header>

<section>
  <div class="abs hero" role="img" aria-label="Bright living room background"></div>
  <div class="abs hero-photo" role="img" aria-label="Photo of a happy woman jumping on a bathroom scale"></div>
  <h2 class="abs slab hero-kicker">Start Your Own Profitable</h2>
  <h1 class="abs slab hero-title">Weight Loss Clinic!</h1>
  <div class="abs hero-copy">
    <p>We are not a weight loss franchise – you are simply buying our business model, training and support for one low fee. Please read about us, look at what we offer and compare us to weight loss franchises in the marketplace.</p>
    <p>We offer you a free market analysis and sample break even analysis for your area.</p>
    <p>We think you will be happy you found us!</p>
  </div>
  <a class="btn" style="left:156px;top:455px;width:132px;height:41px;background:var(--red);font-size:13px">Learn More</a>
  <div class="abs panel">
    <div class="panel-kicker">Start Your Own</div>
    <div class="panel-title">Weight Loss &amp; Wellness Center</div>
    <div class="panel-copy">TrimPath Clinics now offers our model to you so you can add weight loss and wellness programs to your existing medical practice or open a stand alone weight loss and wellness center.<br>We are not a weight loss franchise – you are simply buying our business model, training and support for one low fee. Please read about us, look at what we offer and compare us to weight loss franchises in the marketplace.</div>
  </div>
  <a class="btn" style="left:188px;top:857px;width:117px;height:35px;background:var(--btn-blue);font-size:10px">Learn More</a>
</section>

<section class="abs offer"></section>
<div class="card" style="left:155px;top:1126px"><div class="card-label">One-on-one<br>business &amp;<br>medical training</div></div>
<div class="card" style="left:405px;top:1064px">
  <svg width="76" height="76" viewBox="0 0 76 76" fill="none" stroke="#222" stroke-width="2.5"><path d="M8 30h10l22-12v40L18 46H8z"/><path d="M12 46l4 14h7l-3-14"/><circle cx="38" cy="12" r="6"/><path d="M56 6l8 6-8 6-8-6z"/><circle cx="62" cy="32" r="5"/><path d="M52 50l10-4 4 10-10 4z"/></svg>
  <div class="card-label">Marketing &amp;<br>Advertising<br>Training</div>
</div>
<div class="card" style="left:155px;top:1376px"><div class="card-label">Diets, Patient<br>Protocols &amp;<br>Programs</div></div>
<div class="card" style="left:405px;top:1313px">
  <svg width="76" height="86" viewBox="0 0 76 86" fill="none" stroke="#222" stroke-width="3"><rect x="4" y="4" width="66" height="78" rx="3"/><path d="M14 4v78M14 70h56"/><path d="M40 32l4 8 8 1-6 6 2 8-8-4-8 4 2-8-6-6 8-1z"/><path d="M50 4v14l5-4 5 4V4"/></svg>
  <div class="card-label">Office &amp;<br>Operations<br>Manuals</div>
</div>
<div class="abs rule" style="left:682px;top:1155px"></div>
<h2 class="abs slab offer-title">What We Offer</h2>
<p class="abs offer-copy">Lorem ipsum dolor sit amet, consectetur adipiscing elit. Fusce sit amet massa ante. Duis laoreet maximus enim, vel pharetra urna porta a. Orci varius natoque penatibus et magnis dis parturient montes, nascetur ridiculus mus. In ultricies ipsum pharetra</p>
<ul class="abs ticks">
  <li><svg width="13" height="10" viewBox="0 0 13 10"><path d="M1 5l4 4 7-8" fill="none" stroke="#2f80d8" stroke-width="1.6"/></svg>Lorem ipsum dolor sit amet, consectetur</li>
  <li><svg width="13" height="10" viewBox="0 0 13 10"><path d="M1 5l4 4 7-8" fill="none" stroke="#2f80d8" stroke-width="1.6"/></svg>Lorem ipsum dolor sit amet, consectetur</li>
  <li><svg width="13" height="10" viewBox="0 0 13 10"><path d="M1 5l4 4 7-8" fill="none" stroke="#2f80d8" stroke-width="1.6"/></svg>Lorem ipsum dolor sit amet, consectetur</li>
</ul>
<div class="abs call" style="left:682px;top:1402px">
  <svg width="34" height="34" viewBox="0 0 34 34"><circle cx="17" cy="17" r="15.5" fill="none" stroke="#2f80d8" stroke-width="2"/><path d="M12 10c1-1 2-1 3 0l2 3c.5 1 0 2-1 2.5-.5.5 0 2 1.5 3.5s3 2 3.5 1.5c.5-1 1.5-1.5 2.5-1l3 2c1 1 1 2 0 3-3 3-8 1-12-3s-6-9-2.5-11.5z" fill="#2c4f86"/></svg>
  <div><small>Free Consultation</small><strong>877-555-0142</strong></div>
</div>
<a class="btn" style="left:897px;top:1399px;width:134px;height:41px;background:var(--btn-blue);font-size:14px">Contact Us</a>

<section class="abs steps">
  <h2 class="abs slab steps-title" style="font-weight:500">Get Started Today</h2>
  <div class="step" style="left:122px"><div class="step-num"><span>1</span></div><h3>Contact Us</h3><p>Contact us for more<br>information on our model</p></div>
  <div class="step" style="left:350px"><div class="step-num"><span>2</span></div><h3>Visit Us</h3><p>Schedule a time to visit Atlanta and<br>see our clinics in action</p></div>
  <div class="step" style="left:570px"><div class="step-num"><span>3</span></div><h3>Schedule a Webinar</h3><p>Schedule your one-on-one 20 minute<br>webinar more+</p></div>
  <a class="btn" style="left:339px;top:255px;width:210px;height:39px;background:var(--heading);font-size:12px">Contact Us to Get Started</a>
</section>

<section class="abs compare">
  <h2 class="abs slab compare-title" style="font-weight:500">Compare</h2>
  <div class="pill" style="left:202px;top:91px"><svg width="13" height="10" viewBox="0 0 13 10"><path d="M1 5l4 4 7-8" fill="none" stroke="#fff" stroke-width="1.6"/></svg>No franchise fees</div>
  <div class="pill" style="left:468px;top:91px"><svg width="13" height="10" viewBox="0 0 13 10"><path d="M1 5l4 4 7-8" fill="none" stroke="#fff" stroke-width="1.6"/></svg>No franchise fees</div>
  <div class="pill" style="left:202px;top:136px"><svg width="13" height="10" viewBox="0 0 13 10"><path d="M1 5l4 4 7-8" fill="none" stroke="#fff" stroke-width="1.6"/></svg>No franchise fees</div>
  <div class="pill" style="left:468px;top:136px"><svg width="13" height="10" viewBox="0 0 13 10"><path d="M1 5l4 4 7-8" fill="none" stroke="#fff" stroke-width="1.6"/></svg>No franchise fees</div>
  <div class="pill" style="left:202px;top:182px"><svg width="13" height="10" viewBox="0 0 13 10"><path d="M1 5l4 4 7-8" fill="none" stroke="#fff" stroke-width="1.6"/></svg>No franchise fees</div>
  <div class="pill" style="left:468px;top:182px"><svg width="13" height="10" viewBox="0 0 13 10"><path d="M1 5l4 4 7-8" fill="none" stroke="#fff" stroke-width="1.6"/></svg>No franchise fees</div>
  <div class="pill" style="left:202px;top:227px"><svg width="13" height="10" viewBox="0 0 13 10"><path d="M1 5l4 4 7-8" fill="none" stroke="#fff" stroke-width="1.6"/></svg>No franchise fees</div>
  <div class="pill" style="left:468px;top:227px"><svg width="13" height="10" viewBox="0 0 13 10"><path d="M1 5l4 4 7-8" fill="none" stroke="#fff" stroke-width="1.6"/></svg>No franchise fees</div>
  <a class="btn" style="left:371px;top:282px;width:146px;height:39px;background:var(--red);font-size:12.5px">Compare Now</a>
</section>

<section>
  <div class="abs rule" style="left:156px;top:2489px"></div>
  <h2 class="abs slab contact-title">Contact Us</h2>
  <p class="abs contact-sub">Start your journey today</p>
  <div class="abs contact-item" style="left:156px;top:2612px">
    <svg width="30" height="22" viewBox="0 0 30 22"><rect width="30" height="22" rx="2" fill="#111"/><path d="M2 3l13 10 13-10" fill="none" stroke="#fff" stroke-width="2"/></svg>
    <div>Email<br><b>hello@slimcarecourses.net</b></div>
  </div>
  <div class="abs contact-item" style="left:381px;top:2609px">
    <svg width="30" height="30" viewBox="0 0 30 30"><path d="M5 2c2-2 4-1 5 1l3 5c1 2 0 3-1 4-1 1 1 4 3 6s5 4 6 3c1-1 2-2 4-1l5 3c2 1 3 3 1 5-4 4-11 2-18-5S1 6 5 2z" fill="#111"/></svg>
    <div>Phone number<br><b>877-555-0142</b></div>
  </div>
  <div class="abs contact-photo" role="img" aria-label="Photo of three smiling women in workout clothes against a brick wall"></div>
  <form class="abs form-card">
    <div class="form-head">Send Us Message</div>
    <div class="field" style="top:90px">Name</div>
    <div class="field" style="top:131px">Email</div>
    <div class="field" style="top:171px">Phone</div>
    <div class="field" style="top:212px;height:92px">Message</div>
    <div class="btn" style="left:32px;top:315px;width:92px;height:27px;background:var(--btn-blue);font-size:11px;border-radius:2px">Submit</div>
  </form>
</section>

<section class="partner-area">
  <div class="abs partner"></div>
  <div class="abs partner-photo" role="img" aria-label="Photo of two fit young women pointing toward the text"></div>
  <div class="abs slab partner-kicker">Doctor's Medical &nbsp;Business Opportunity</div>
  <h2 class="abs slab partner-title">Weight Loss Partnership</h2>
  <div class="abs partner-copy">
    <p>Our exclusive, proprietary game-changing treatment plan includes new <b style="font-size:12px">FDA approved</b> custom-blended, patient-specific prescription medication. This medication is tailor-made for each patient and shipped directly from our licensed US pharmacy.</p>
    <p>We use a red-hot new treatment plan with FDA-approved custom-blended prescription medicine from our exclusive pharmacies that let patients avoid costly, risky surgery and the same old stimulant-based meds that have been around forever — at prices nobody can match!</p>
  </div>
  <div class="abs offer-icon">
    <svg width="78" height="78" viewBox="0 0 78 78" fill="none" stroke="#2b86de" stroke-width="4" stroke-linecap="round"><path d="M18 54L52 20"/><path d="M26 38l8 8M32 32l8 8M38 26l8 8"/><circle cx="56" cy="56" r="11" fill="#2b86de" stroke="none"/><path d="M51 51l10 10M61 51L51 61" stroke="#fff" stroke-width="3"/></svg>
  </div>
  <div class="abs offer-detail">
    <b style="font-size:10.5px">We truly offer:</b><br>
    <span style="display:block;font-size:12.5px;margin:8px 0 6px">SURGICAL RESULTS WITHOUT SURGERY</span>
    Doctors call it a liquid gastric bypass!<br>Taken once a week, this medication allows patients to eat less while still feeling full...and still getting their recommended daily nutrition.
  </div>
</section>

<section class="abs invest">
  <h2 class="slab invest-title">Interested In Investing?</h2>
  <a class="btn" style="left:529px;top:73px;width:140px;height:42px;background:var(--white);color:var(--heading);font-size:14px">Contact Us</a>
  <p class="slab invest-foot">To set up a FREE, no obligation consultation.</p>
</section>

</body>
</html>
```